KTR Motorhaus Automotive Repair and Service Shop

I need an informative and interactive website for my automotive service and repair shop. The website must give information about the shop, as well as the ability to make bookings and a forums page for our users to use and set up an account with us, in which we can give promotions via email. We are located in Pompano Beach Florida and our company name is KTR Motorhaus. Our color scheme is a red for accent and grey (neutral color) as a base. The design must communicate our message and be able to grow should we decide to retail parts in the future. One of the websites I take the highest inspiration from is http://www.lanvexbodyshop.example/. Although I do not have as nearly as many certifications as them. Attached are some images of our shop so you can see how clean and modern our building is, and I would like our website to match our feel. Thank you.

Target Market(s)

Automotive Enthusiasts

Industry/Entity Type

Automotive

Contact Information for Business Card

KTR Motorhaus /954 718 6402 /rohan@ktrmotorhaus.example/ 512 NE 9th St Pompano Beach FL 33062/ any other info needed please ask me

Coding

Coded - Design and coding required

Number of Pages Required

5+ page

Font styles to use
Sans Serif

Requirements
Must have
• Name, logo, contact info, location, phone number
Nice to have
• Building is very modern, would like a business card to match
Should not have
• Not to playful or vibrant

```html
<!DOCTYPE html>
<html lang="en">
<head>
<meta charset="utf-8">
<title>KTR Motorhaus</title>
<link rel="stylesheet" href="https://fonts.googleapis.com/css2?family=Anton&family=Roboto:ital,wght@0,400;0,500;0,700;1,400&display=swap">
<style>
:root{
  --red:#e31b1b;
  --red-dark:#b80f0f;
  --ink:#111;
  --text:#222;
  --muted:#7a7a7a;
  --line:#e5e5e5;
  --white:#fff;
  --footer:#0d0d0d;
}
*{box-sizing:border-box;margin:0;padding:0}
html,body{width:1200px;height:4191px;overflow:hidden}
body{position:relative;background:var(--white);font-family:"Roboto",Arial,sans-serif;color:var(--text)}
.abs{position:absolute}
.display{font-family:"Anton","Impact",sans-serif;text-transform:uppercase;font-weight:400;letter-spacing:.2px}
.accent{color:var(--red)}
.photo{position:absolute}
.btn{position:absolute;background:var(--red);color:var(--white);font-family:"Anton",sans-serif;font-size:14px;text-transform:uppercase;display:flex;align-items:center;justify-content:center;gap:5px}
.btn svg{width:11px;height:11px}

/* header */
.topline{top:0;left:0;width:1200px;height:4px;background:var(--red)}
.header{top:0;left:0;width:1200px;height:109px;background:var(--white)}
.top-contact{top:22px;font-size:13px;color:var(--muted);display:flex;align-items:center;gap:6px}
.top-contact svg{width:12px;height:12px;fill:var(--muted)}
.nav-item{top:68px;font-family:"Anton",sans-serif;font-size:16px;color:var(--ink);text-transform:uppercase}
.nav-item.active{color:var(--red)}
.brand-plate{left:449px;top:0;width:301px;height:174px}
.brand-name{left:449px;top:14px;width:301px;text-align:center;font-family:"Anton",sans-serif;font-size:30px;color:var(--ink);text-transform:uppercase}

/* hero */
.hero{top:109px;left:0;width:1200px;height:598px}
.hero-photo{left:0;top:0;width:1200px;height:598px;background:linear-gradient(110deg,#6a6e72 0%,#9a9ea2 35%,#c0b8b8 60%,#8b3a3a 80%,#5c5f63 100%)}
.hero-panel{left:353px;top:143px;width:494px;height:241px;background:rgba(30,30,30,.62)}
.hero-title{left:353px;top:172px;width:494px;text-align:center;font-size:56px;color:var(--white)}
.hero-sub{left:353px;top:238px;width:494px;text-align:center;font-size:17px;line-height:26px;color:var(--white)}
.dots{left:578px;top:496px;display:flex;gap:5px}
.dots span{width:12px;height:12px;border-radius:50%;background:var(--white)}
.dots span:first-child{background:var(--red)}

/* about */
.section-title{left:0;width:1200px;text-align:center;color:var(--ink)}
.about-text{left:160px;top:872px;width:880px;text-align:center;font-size:13.5px;line-height:25.5px;color:var(--muted)}
.feature{top:1078px;width:200px;text-align:center;font-size:18px;color:var(--ink)}
.feature svg{display:block;margin:0 auto 12px;width:56px;height:56px}

/* services */
.services-band{left:0;top:1418px;width:1200px;height:600px;background:var(--ink)}
.service-card{top:1626px;width:286px;height:374px}
.service-card .photo{left:0;top:0;width:100%;height:100%}
.service-card .cap{position:absolute;left:0;bottom:24px;width:100%;text-align:center;font-family:"Anton",sans-serif;font-size:16px;color:var(--white);text-transform:uppercase}
.pager{top:2038px;left:466px;display:flex;align-items:center;gap:20px;font-size:14px;color:var(--ink)}
.pager .num{color:var(--red)}

/* why */
.why-sub{left:642px;top:2220px;width:460px;font-family:"Anton",sans-serif;font-size:15px;line-height:26px;color:var(--ink);text-transform:uppercase}
.why-text{left:642px;top:2280px;width:470px;font-size:13.5px;line-height:25.7px;color:var(--muted);text-align:justify}

/* reviews */
.reviews{left:0;top:2562px;width:1200px;height:448px;background:linear-gradient(100deg,#d91414 0%,#f01c1c 45%,#e01818 70%,#c41010 100%)}
.avatar{left:222px;top:2747px;width:168px;height:168px;border-radius:50%;background:radial-gradient(circle at 50% 40%,#c9c9cf,#3f5e8e 75%)}
.stars{left:412px;top:2741px;display:flex;gap:3px}
.stars svg{width:14px;height:14px;fill:#ffd21f}
.quote{left:412px;top:2767px;width:630px;font-size:13px;line-height:26px;font-style:italic;color:var(--white)}
.reviewer{left:412px;top:2852px;font-size:17px;line-height:26px;color:var(--white)}
.arrow{top:2787px;width:28px;height:34px}

/* blog */
.blog-card{top:3176px;width:312px}
.blog-card .photo{position:relative;width:312px;height:201px;border:1px solid var(--line)}
.blog-date{margin-top:24px;font-family:"Anton",sans-serif;font-size:14px;letter-spacing:4px;color:var(--muted);display:flex;align-items:center;gap:6px}
.blog-date svg{width:13px;height:13px;fill:var(--red)}
.blog-title{margin-top:10px;font-size:18px;font-weight:500;color:var(--ink);text-transform:uppercase}
.blog-text{margin-top:8px;font-size:13.5px;line-height:26px;color:var(--muted);width:320px}
.blog-more{margin-top:10px;font-size:13px;font-weight:700;color:var(--ink);text-transform:uppercase;display:flex;align-items:center;gap:4px}
.blog-more svg{width:12px;height:12px}

/* footer */
.footer{left:0;top:3678px;width:1200px;height:513px;background:var(--footer)}
.footer-head{font-size:20px;font-weight:500;color:var(--white);text-transform:uppercase}
.footer-lead{left:117px;top:3818px;font-size:15px;color:var(--white)}
.field{height:42px;border:1px solid #bbb;color:var(--white);font-size:13px;padding:11px 14px}
.submit{left:119px;top:3982px;width:454px;height:50px;background:var(--red);color:var(--white);font-size:18px;font-weight:700;display:flex;align-items:center;justify-content:center}
.contact-row{left:652px;display:flex;gap:14px;font-size:13.5px;line-height:22px;color:var(--white)}
.contact-row svg{width:18px;height:18px;flex:none;margin-top:2px;fill:none;stroke:var(--white);stroke-width:1.6}
.quick-link{left:959px;font-size:14px;color:var(--white)}
.footer-rule{left:0;top:4070px;width:1200px;height:1px;background:#2a2a2a}
.copyright{left:0;top:4118px;width:1200px;text-align:center;font-size:14px;color:var(--white)}
</style>
</head>
<body>

<!-- header -->
<div class="abs header"></div>
<div class="abs topline"></div>
<div class="abs top-contact" style="left:120px"><svg viewBox="0 0 24 24"><path d="M6.6 10.8c1.4 2.8 3.8 5.1 6.6 6.6l2.2-2.2c.3-.3.7-.4 1-.2 1.1.4 2.3.6 3.6.6.6 0 1 .4 1 1V20c0 .6-.4 1-1 1C10.6 21 3 13.4 3 4c0-.6.4-1 1-1h3.5c.6 0 1 .4 1 1 0 1.3.2 2.5.6 3.6.1.3 0 .7-.2 1z"/></svg>954 718 6402</div>
<div class="abs top-contact" style="left:246px"><svg viewBox="0 0 24 24"><path d="M2 5h20v14H2z M2 5l10 8 10-8" fill="none" stroke="#7a7a7a" stroke-width="2"/></svg>rohan@ktrmotorhaus.example</div>
<div class="abs top-contact" style="left:836px"><svg viewBox="0 0 24 24"><path d="M3 3h18v18H3z M7 12l4 4 7-8" fill="none" stroke="#7a7a7a" stroke-width="2"/></svg>Book now</div>
<div class="abs top-contact" style="left:975px"><svg viewBox="0 0 24 24"><circle cx="12" cy="12" r="10" fill="none" stroke="#7a7a7a" stroke-width="2"/><circle cx="12" cy="10" r="3.5"/><path d="M5.5 18.5c1.8-2.5 4-3.5 6.5-3.5s4.7 1 6.5 3.5"/></svg>Login/Register</div>
<div class="abs nav-item active" style="left:110px">Home</div>
<div class="abs nav-item" style="left:199px">About Us</div>
<div class="abs nav-item" style="left:311px">Services</div>
<div class="abs nav-item" style="left:799px">Carrers</div>
<div class="abs nav-item" style="left:908px">Reviews</div>
<div class="abs nav-item" style="left:1014px">Contact Us</div>

<!-- hero -->
<div class="abs hero">
  <div class="photo hero-photo" role="img" aria-label="Clean modern workshop with technicians servicing a red hatchback on a lift"></div>
  <svg class="abs" style="left:0;top:540px" width="1200" height="58" viewBox="0 0 1200 58"><polygon points="0,0 1200,40 1200,58 0,58" fill="var(--white)"/><polygon points="0,20 0,58 260,58" fill="var(--red)"/><polygon points="0,0 700,24 0,40" fill="var(--red-dark)" opacity=".9"/></svg>
  <div class="abs hero-panel"></div>
  <div class="abs hero-title display">KTR Motorhaus</div>
  <div class="abs hero-sub">An informative and interactive website for my<br>automotive service and repair shops.</div>
  <div class="btn" style="left:540px;top:307px;width:120px;height:44px">Get Started</div>
  <div class="abs dots"><span></span><span></span><span></span></div>
</div>
<svg class="abs brand-plate" viewBox="0 0 301 174"><polygon points="0,0 301,0 301,140 150,174 0,140" fill="var(--white)"/></svg>
<div class="abs brand-name">KTR Motorhaus</div>

<!-- about -->
<h2 class="abs section-title display" style="top:800px;font-size:42px">About <span class="accent">KTR Motorhaus</span></h2>
<p class="abs about-text">Lorem ipsum dolor sit amet, consectetur adipiscing elit, sed do eiusmod tempor incididunt ut labore et dolore magna aliqua. Ut enim ad minim veniam, quis nostrud exercitation ullamco laboris nisi ut aliquip ex ea commodo consequat. Duis aute irure dolor in reprehenderit in voluptate velit esse cillum dolore eu fugiat nulla pariatur. Excepteur sint occaecat cupidatat non proident, sunt in culpa qui officia deserunt mollit anim id est laborum.</p>
<div class="btn" style="left:540px;top:1003px;width:120px;height:46px">Learn More <svg viewBox="0 0 24 24"><circle cx="12" cy="12" r="11" fill="#fff"/><path d="M7 12h9M12 7l5 5-5 5" stroke="var(--red)" stroke-width="3" fill="none"/></svg></div>

<div class="abs feature" style="left:227px">
  <svg viewBox="0 0 56 56"><path d="M4 38V28l5-10h18l5 10v10z" fill="var(--ink)"/><circle cx="12" cy="40" r="4" fill="#fff" stroke="var(--ink)" stroke-width="2"/><circle cx="26" cy="40" r="4" fill="#fff" stroke="var(--ink)" stroke-width="2"/><polygon points="40,10 54,42 26,42" fill="#fff" stroke="var(--red)" stroke-width="3.5"/><rect x="38.5" y="20" width="3" height="12" fill="var(--red)"/><rect x="38.5" y="35" width="3" height="3" fill="var(--red)"/></svg>Lorem Ipsum</div>
<div class="abs feature" style="left:500px">
  <svg viewBox="0 0 56 56"><circle cx="22" cy="24" r="14" fill="none" stroke="var(--ink)" stroke-width="7" stroke-dasharray="5 4"/><circle cx="22" cy="24" r="6" fill="var(--ink)"/><path d="M36 16l12 24" stroke="var(--red)" stroke-width="6" stroke-linecap="round"/><path d="M20 48l26-26" stroke="var(--red)" stroke-width="6" stroke-linecap="round"/></svg>Lorem Ipsum</div>
<div class="abs feature" style="left:773px">
  <svg viewBox="0 0 56 56"><rect x="24" y="6" width="26" height="42" fill="#fff" stroke="var(--red)" stroke-width="3"/><rect x="31" y="3" width="12" height="6" fill="var(--red)"/><path d="M29 18h4M36 18h10M29 26h4M36 26h10M29 34h4M36 34h10" stroke="var(--ink)" stroke-width="2.5"/><path d="M4 46V36l4-8h14v18z" fill="var(--ink)"/><circle cx="10" cy="47" r="3.5" fill="#fff" stroke="var(--ink)" stroke-width="2"/></svg>Lorem Ipsum</div>

<!-- services -->
<div class="abs services-band"></div>
<svg class="abs" style="left:0;top:1405px" width="1200" height="60" viewBox="0 0 1200 60"><polygon points="0,13 1200,13 1200,60 0,60" fill="var(--ink)"/><polygon points="760,36 1200,0 1200,20 900,40" fill="var(--red)"/></svg>
<div class="photo" style="left:102px;top:1244px;width:318px;height:219px;background:linear-gradient(180deg,#7d7d7d,#3b3b3b)" role="img" aria-label="Illustration of a grey sports coupe, front view"></div>
<div class="photo" style="left:439px;top:1250px;width:320px;height:213px;background:linear-gradient(180deg,#1f7a56,#0e3d2b)" role="img" aria-label="Illustration of a green classic sports car, front view"></div>
<div class="photo" style="left:777px;top:1270px;width:312px;height:193px;background:linear-gradient(180deg,#f03a3a,#9e0f0f)" role="img" aria-label="Illustration of a red roadster, front view"></div>

<h2 class="abs section-title display" style="top:1536px;font-size:52px;color:var(--white)">Our <span class="accent">Services</span></h2>
<div class="abs service-card" style="left:7px"><div class="photo" style="background:linear-gradient(180deg,#8a8f96,#3f444c)" role="img" aria-label="SUV raised on a service lift in the workshop"></div><div class="cap">Complete Auto Repair and Service</div></div>
<div class="abs service-card" style="left:306px"><div class="photo" style="background:linear-gradient(180deg,#4a4f5a,#1f2227 70%,#3a5fa8)" role="img" aria-label="Fresh engine oil being poured through a funnel"></div><div class="cap">Full Diagnostics and Repairs</div></div>
<div class="abs service-card" style="left:606px"><div class="photo" style="background:linear-gradient(180deg,#c7cbcf,#6f747a)" role="img" aria-label="Mechanic working under an open car bonnet"></div><div class="cap">Custom Work</div></div>
<div class="abs service-card" style="left:906px"><div class="photo" style="background:linear-gradient(180deg,#2e5aa0,#1a2b47)" role="img" aria-label="Hands inspecting engine parts during repair"></div><div class="cap">Engine Repair</div></div>

<div class="abs pager">
  <svg width="56" height="30" viewBox="0 0 56 30"><path d="M55 15H3M15 3L3 15l12 12" stroke="var(--red)" stroke-width="2" fill="none"/></svg>
  <span>Prev</span><span class="num">1</span><span>Next</span>
  <svg width="56" height="30" viewBox="0 0 56 30"><path d="M1 15h52M41 3l12 12-12 12" stroke="var(--ink)" stroke-width="2" fill="none"/></svg>
</div>

<!-- why choose us -->
<div class="photo" style="left:89px;top:2171px;width:521px;height:284px;background:radial-gradient(ellipse at 50% 55%,#e9eaec 0%,#c5c8cc 55%,#ffffff 78%)" role="img" aria-label="White SUV, three-quarter front view"></div>
<h2 class="abs display" style="left:642px;top:2155px;font-size:40px;color:var(--ink)">Why <span class="accent">Choose Us</span></h2>
<div class="abs why-sub">Lorem ipsum dolor sit amet, consectetur adipiscing elit, sed do eiusmod tempor incididunt ut labore et</div>
<p class="abs why-text">Lorem ipsum dolor sit amet, consectetur adipiscing elit, sed do eiusmod tempor incididunt ut labore et dolore magna aliqua. Ut enim ad minim veniam, quis nostrud exercitation ullamco laboris nisi ut aliquip ex ea commodo consequat. Duis aute irure dolor in reprehenderit in voluptate velit esse cillum dolore eu fugiat nulla pariatur.</p>
<div class="btn" style="left:642px;top:2423px;width:122px;height:44px">Learn More <svg viewBox="0 0 24 24"><circle cx="12" cy="12" r="11" fill="#fff"/><path d="M7 12h9M12 7l5 5-5 5" stroke="var(--red)" stroke-width="3" fill="none"/></svg></div>

<!-- reviews -->
<div class="abs reviews" role="img" aria-label="Red-toned workshop scene behind the customer reviews"></div>
<h2 class="abs section-title display" style="top:2655px;font-size:40px;color:var(--white)">Reviews</h2>
<div class="abs avatar" role="img" aria-label="Portrait of a smiling customer in a blue suit"></div>
<div class="abs stars">
  <svg viewBox="0 0 24 24"><path d="M12 2l3 7h7l-5.5 4.5 2 7.5-6.5-4.5L5.5 21l2-7.5L2 9h7z"/></svg>
  <svg viewBox="0 0 24 24"><path d="M12 2l3 7h7l-5.5 4.5 2 7.5-6.5-4.5L5.5 21l2-7.5L2 9h7z"/></svg>
  <svg viewBox="0 0 24 24"><path d="M12 2l3 7h7l-5.5 4.5 2 7.5-6.5-4.5L5.5 21l2-7.5L2 9h7z"/></svg>
  <svg viewBox="0 0 24 24"><path d="M12 2l3 7h7l-5.5 4.5 2 7.5-6.5-4.5L5.5 21l2-7.5L2 9h7z"/></svg>
  <svg viewBox="0 0 24 24"><path d="M12 2l3 7h7l-5.5 4.5 2 7.5-6.5-4.5L5.5 21l2-7.5L2 9h7z"/></svg>
</div>
<p class="abs quote">“Lorem ipsum dolor sit amet, consectetur adipiscing elit, sed do eiusmod tempor incididunt ut labore et dolore magna aliqua. Ut enim ad minim veniam, quis nostrud exercitation ullamco laboris nisi ut aliquip ex ea com modo consequat.Lorem ipsum dolor sit amet, consectetur adipiscing”</p>
<div class="abs reviewer">- Mark Ellison<br>Lorem ipsum dolor</div>
<svg class="abs arrow" style="left:48px" viewBox="0 0 28 34"><path d="M20 3L7 17l13 14" stroke="#fff" stroke-width="4" fill="none"/></svg>
<svg class="abs arrow" style="left:1120px" viewBox="0 0 28 34"><path d="M8 3l13 14L8 31" stroke="#fff" stroke-width="4" fill="none"/></svg>

<!-- blog -->
<h2 class="abs section-title display" style="top:3098px;font-size:40px">Our <span class="accent">Latest Blog</span></h2>

<div class="abs blog-card" style="left:111px">
  <div class="photo" style="background:linear-gradient(135deg,#5c6068,#2c2f35 60%,#8b1e1e)" role="img" aria-label="Mechanic standing beside an open engine bay"></div>
  <div class="blog-date"><svg viewBox="0 0 24 24"><path d="M3 5h18v16H3z M3 9h18" fill="none" stroke="var(--red)" stroke-width="2.5"/><rect x="6" y="2" width="3" height="5"/><rect x="15" y="2" width="3" height="5"/></svg>January 30,2020</div>
  <div class="blog-title">Lorem ipsum dolor sit amet</div>
  <p class="blog-text">Lorem ipsum dolor sit amet, consectetur adipi scing elit, sed do eiusmod tempor incididunt ut labore et dolore magna aliqua.</p>
  <div class="blog-more">Continue Reading <svg viewBox="0 0 24 24"><circle cx="12" cy="12" r="11"/><path d="M7 12h9M12 7l5 5-5 5" stroke="#fff" stroke-width="3" fill="none"/></svg></div>
</div>
<div class="abs blog-card" style="left:444px">
  <div class="photo" style="background:linear-gradient(135deg,#3a3d44,#6b6f76 50%,#a08a6a)" role="img" aria-label="Two mechanics working under a raised car"></div>
  <div class="blog-date"><svg viewBox="0 0 24 24"><path d="M3 5h18v16H3z M3 9h18" fill="none" stroke="var(--red)" stroke-width="2.5"/><rect x="6" y="2" width="3" height="5"/><rect x="15" y="2" width="3" height="5"/></svg>January 30,2020</div>
  <div class="blog-title">Lorem ipsum dolor sit amet</div>
  <p class="blog-text">Lorem ipsum dolor sit amet, consectetur adipi scing elit, sed do eiusmod tempor incididunt ut labore et dolore magna aliqua.</p>
  <div class="blog-more">Continue Reading <svg viewBox="0 0 24 24"><circle cx="12" cy="12" r="11"/><path d="M7 12h9M12 7l5 5-5 5" stroke="#fff" stroke-width="3" fill="none"/></svg></div>
</div>
<div class="abs blog-card" style="left:776px">
  <div class="photo" style="background:linear-gradient(135deg,#d8d8d8,#9a9ea4 45%,#c4161c 75%,#2b3a5c)" role="img" aria-label="Mechanic shaking hands with a customer beside a red car"></div>
  <div class="blog-date"><svg viewBox="0 0 24 24"><path d="M3 5h18v16H3z M3 9h18" fill="none" stroke="var(--red)" stroke-width="2.5"/><rect x="6" y="2" width="3" height="5"/><rect x="15" y="2" width="3" height="5"/></svg>January 30,2020</div>
  <div class="blog-title">Lorem ipsum dolor sit amet</div>
  <p class="blog-text">Lorem ipsum dolor sit amet, consectetur adipi scing elit, sed do eiusmod tempor incididunt ut labore et dolore magna aliqua.</p>
  <div class="blog-more">Continue Reading <svg viewBox="0 0 24 24"><circle cx="12" cy="12" r="11"/><path d="M7 12h9M12 7l5 5-5 5" stroke="#fff" stroke-width="3" fill="none"/></svg></div>
</div>

<!-- footer -->
<div class="abs footer"></div>
<div class="abs footer-head" style="left:120px;top:3770px">KTR Motorhaus</div>
<div class="abs footer-lead">Lorem ipsum dolor sit amet, consectetur adipiscing elit</div>
<div class="abs field" style="left:119px;top:3858px;width:218px">Name</div>
<div class="abs field" style="left:356px;top:3858px;width:217px">E - Mail</div>
<div class="abs field" style="left:119px;top:3919px;width:218px">Subject</div>
<div class="abs field" style="left:356px;top:3919px;width:217px">Message</div>
<div class="abs submit">SUBMIT</div>

<div class="abs footer-head" style="left:652px;top:3764px">Contact Us</div>
<div class="abs contact-row" style="top:3819px"><svg viewBox="0 0 24 24"><path d="M12 22s7-7 7-12a7 7 0 0 0-14 0c0 5 7 12 7 12z"/><circle cx="12" cy="10" r="2.5"/></svg><span>512 NE 9th St Pompano<br>Beach FL 33062</span></div>
<div class="abs contact-row" style="top:3873px"><svg viewBox="0 0 24 24"><path d="M6.6 10.8c1.4 2.8 3.8 5.1 6.6 6.6l2.2-2.2c.3-.3.7-.4 1-.2 1.1.4 2.3.6 3.6.6.6 0 1 .4 1 1V20c0 .6-.4 1-1 1C10.6 21 3 13.4 3 4c0-.6.4-1 1-1h3.5c.6 0 1 .4 1 1 0 1.3.2 2.5.6 3.6.1.3 0 .7-.2 1z"/></svg><span>Phone: 954 718 6402</span></div>
<div class="abs contact-row" style="top:3919px"><svg viewBox="0 0 24 24" style="fill:#fff;stroke:none"><circle cx="12" cy="12" r="10"/><path d="M12 6v6h5" stroke="#0d0d0d" stroke-width="2.4" fill="none"/></svg><span>Time : Mon-fri 8am-5pm Mst</span></div>
<div class="abs contact-row" style="top:3971px"><svg viewBox="0 0 24 24"><path d="M2 5h20v14H2z M2 5l10 8 10-8"/></svg><span>Email: rohan@ktrmotorhaus.example</span></div>

<div class="abs footer-head" style="left:959px;top:3764px">Quick Links</div>
<div class="abs quick-link" style="top:3819px">Home</div>
<div class="abs quick-link" style="top:3848px">About Us</div>
<div class="abs quick-link" style="top:3877px">Services</div>
<div class="abs quick-link" style="top:3906px">Our Clients</div>
<div class="abs quick-link" style="top:3935px">News</div>
<div class="abs quick-link" style="top:3964px">Contact Us</div>

<div class="abs footer-rule"></div>
<div class="abs copyright">(c) 2020 KTR Motorhaus | All Rights Reserved | Terms and Conditions</div>

</body>
</html>
```